We are a organisation that provide outdoor adventure based tours to international students in New Ze

We are a Waikato New Zealand based company that runs adventure and outdoor tours around New Zealand. Activities included in our tours are mountain biking, rafting, sea kayaking, surfing/SUPing, luge, high ropes course, tramping, snorkelling and cultural activities. We need a Name/Logo, advertisement and information Flyers that we can give to the students/customers ASAP. We still haven't come up with a name so are hoping that designers can be more creative than we are. we are running our fist trip Dec 15th-22nd 2013.

Attached are some bits of information that we need to be included in the flyer. We need to get the 'Brightwater Tour' filled up first and the 'Kestrel's Cove Tour' will be later.

We want it to be an exciting and edgy design with an 'outdoor' feel to it. There is the potential for this design to be expanded into our website.

The brochure/ Flyer can come in any creative format.

Target Market(s)

High school aged students. We will be expanding to University students in the future. We also need to make sure that this is appealing to the parents. It will be them who will agree to them going on the trips after all.

Industry/Entity Type

It Company

Requirements
Must have
• Our Contact details.
Booking Info
Tour information from attached.
Nice to have
• Photos can use the ones we have put into the attachment or other images from the outdoors that designers can source to make it look good.

```html
<!DOCTYPE html>
<html lang="en">
<head>
<meta charset="utf-8">
<title>Take the path less travelled – Trailmark Tours</title>
<link rel="stylesheet" href="https://fonts.googleapis.com/css2?family=Lobster&family=Open+Sans:ital,wght@0,400;0,600;0,700;1,400&family=Noto+Serif:ital,wght@1,700&display=swap">
<style>
:root{
  --sky-top:#1e3f9a;
  --sky-mid:#5d8fd8;
  --snow:#eef3fa;
  --navy:#1d2f73;
  --panel-blue:#3f5e90;
  --grass:#6fb43f;
  --teal:#2d9a9c;
  --teal-dark:#1f7f86;
  --teal-light:#49b3b2;
  --card:#ebe3b5;
  --ink:#2a2a2a;
  --orange:#f07722;
  --footer:#231f20;
  --salmon:#f2876a;
  --white:#ffffff;
}
*{box-sizing:border-box;margin:0;padding:0}
html,body{width:927px;height:1200px;overflow:hidden;background:var(--white)}
.flyer{position:relative;width:927px;height:1200px;overflow:hidden;font-family:"Open Sans",Arial,sans-serif;background:var(--panel-blue)}
.hero{position:absolute;left:0;top:0;width:927px;height:680px;
  background:
    radial-gradient(ellipse 340px 260px at 360px 60px,rgba(255,255,255,.9),rgba(255,255,255,0) 70%),
    linear-gradient(160deg,var(--snow) 0%,#c9d8ee 30%,var(--sky-mid) 45%,var(--sky-top) 75%,#16307d 100%);}
.grass-band{position:absolute;left:0;top:522px;width:300px;height:160px;background:var(--grass)}
.accents{position:absolute;left:0;top:0}
.book{position:absolute;right:52px;top:38px;color:var(--white);text-align:right}
.book-line{font-weight:700;font-size:19px;letter-spacing:.3px}
.book-line .phone{font-size:30px;margin-left:10px;vertical-align:-2px}
.book-email{font-weight:700;font-size:15px;margin-top:-2px}
.headline{position:absolute;left:368px;top:118px;font-family:"Lobster",cursive;font-weight:400;font-size:78px;line-height:70px;color:var(--white);white-space:nowrap;
  transform:rotate(-3deg) skewX(-6deg);transform-origin:left top;
  text-shadow:-3px 0 var(--navy),3px 0 var(--navy),0 3px var(--navy),0 -3px var(--navy),6px 7px 2px rgba(10,20,60,.6)}
.headline span{display:block}
.headline .l2{margin-left:70px}
.photo{position:absolute;background:var(--white);padding:10px;box-shadow:3px 5px 10px rgba(0,0,0,.45)}
.photo .fill{width:100%;height:100%}
.photo-lake{left:98px;top:402px;width:208px;height:272px;transform:rotate(7deg)}
.photo-lake .fill{background:linear-gradient(180deg,#bcd9ef 0%,#6fa3c7 35%,#3f7fa8 55%,#5d8f3d 72%,#3f6a2a 100%)}
.photo-raft{left:280px;top:318px;width:170px;height:262px;transform:rotate(4deg)}
.photo-raft .fill{background:linear-gradient(180deg,#6b8060 0%,#5a7a8a 40%,#d9e6ef 70%,#f3f6f8 100%)}
.photo-group{left:578px;top:888px;width:338px;height:268px;transform:rotate(5deg)}
.photo-group .fill{background:linear-gradient(180deg,#d6e6f3 0%,#9cc1dd 30%,#5c8d78 45%,#4d6a5c 60%,#8d8a82 100%)}
.card{position:absolute;left:369px;top:333px;width:560px;height:478px;background:var(--card);transform:rotate(-11.5deg);
  box-shadow:4px 6px 12px rgba(0,0,0,.4);padding:26px 30px 0 30px;color:var(--ink)}
.steps{display:flex;align-items:flex-end;gap:14px;height:52px}
.step{display:flex;align-items:center;gap:8px;font-weight:700;font-size:16px;line-height:17px;white-space:nowrap}
.step-num{flex:none;width:28px;height:28px;border-radius:50%;background:var(--orange);color:var(--white);font-size:19px;text-align:center;line-height:28px}
.step:nth-child(2){position:relative;top:-10px}
.step:nth-child(3){position:relative;top:-20px}
.card-lead{font-weight:700;font-size:18px;line-height:24px;margin-top:24px;white-space:nowrap}
.benefits{list-style:none;margin-top:18px;margin-left:16px}
.benefits li{position:relative;padding-left:20px;font-weight:700;font-size:14px;line-height:19px;white-space:nowrap}
.benefits li svg{position:absolute;left:0;top:3px}
.card p{font-size:14px;line-height:20px;margin-top:14px;margin-left:16px;white-space:nowrap}
.card-cta{font-weight:700;font-size:19px;line-height:22px;margin-top:22px;margin-left:16px;white-space:nowrap}
.panel-title{position:absolute;left:57px;top:726px;font-family:"Noto Serif",Georgia,serif;font-style:italic;font-weight:700;font-size:23px;line-height:30px;color:var(--white);white-space:nowrap}
.panel-title span,.panel-body span{display:block}
.panel-body{position:absolute;left:55px;top:883px;color:var(--white);font-size:14px;line-height:19.5px;white-space:nowrap}
.panel-body p+p{margin-top:19px}
.footer{position:absolute;left:0;top:1088px;width:927px;height:112px;background:var(--footer)}
.brand{position:absolute;left:44px;top:24px;display:flex;align-items:center;gap:10px;color:var(--salmon);font-weight:700;font-size:28px;line-height:32px}
.brand-dot{flex:none;width:18px;height:18px;border-radius:50%;background:var(--salmon)}
.divider{position:absolute;left:240px;top:20px;width:2px;height:74px;background:var(--white)}
.contact{position:absolute;left:276px;top:36px;color:var(--white);font-size:16px;line-height:20px}
.contact strong{display:block;font-size:19px;letter-spacing:.5px}
</style>
</head>
<body>
<main class="flyer">
  <div class="hero" role="img" aria-label="Photo of a skier carving down a snowy mountain slope under a bright blue sky"></div>
  <div class="grass-band"></div>
  <svg class="accents" width="927" height="1200" viewBox="0 0 927 1200" aria-hidden="true">
    <polygon points="700,780 927,700 927,1088 800,1088" fill="var(--teal)"/>
    <polygon points="700,780 927,760 927,880" fill="var(--teal-light)"/>
    <polygon points="760,1088 927,940 927,1088" fill="var(--teal-dark)"/>
  </svg>

  <div class="book">
    <div class="book-line">BOOK NOW ! <span class="phone">02 118 40 562</span></div>
    <div class="book-email">rowan.ashby@trailmail.co.nz</div>
  </div>

  <h1 class="headline"><span>Take the path</span><span class="l2">less travelled</span></h1>

  <div class="photo photo-lake"><div class="fill" role="img" aria-label="Photo of a calm lake with a grassy shore and bush-covered hills"></div></div>
  <div class="photo photo-raft"><div class="fill" role="img" aria-label="Photo of students white-water rafting in a yellow raft"></div></div>

  <section class="card">
    <div class="steps">
      <div class="step"><span class="step-num">1</span>Love the<br>outdoors?</div>
      <div class="step"><span class="step-num">2</span>Want some better stories<br>about your NZ exchange?</div>
      <div class="step"><span class="step-num">3</span>Check<br>us out!!</div>
    </div>
    <div class="card-lead">Our tours offer a platform for foreign students to …</div>
    <ul class="benefits">
      <li><svg width="13" height="13" viewBox="0 0 13 13"><circle cx="6.5" cy="6.5" r="6" fill="none" stroke="var(--orange)" stroke-width="1.5"/><path d="M3.5 6.5h5M6.5 4l2.5 2.5L6.5 9" fill="none" stroke="var(--orange)" stroke-width="1.6"/></svg>Build confidence</li>
      <li><svg width="13" height="13" viewBox="0 0 13 13"><circle cx="6.5" cy="6.5" r="6" fill="none" stroke="var(--orange)" stroke-width="1.5"/><path d="M3.5 6.5h5M6.5 4l2.5 2.5L6.5 9" fill="none" stroke="var(--orange)" stroke-width="1.6"/></svg>Create positive relationships</li>
      <li><svg width="13" height="13" viewBox="0 0 13 13"><circle cx="6.5" cy="6.5" r="6" fill="none" stroke="var(--orange)" stroke-width="1.5"/><path d="M3.5 6.5h5M6.5 4l2.5 2.5L6.5 9" fill="none" stroke="var(--orange)" stroke-width="1.6"/></svg>Experience new cultures</li>
      <li><svg width="13" height="13" viewBox="0 0 13 13"><circle cx="6.5" cy="6.5" r="6" fill="none" stroke="var(--orange)" stroke-width="1.5"/><path d="M3.5 6.5h5M6.5 4l2.5 2.5L6.5 9" fill="none" stroke="var(--orange)" stroke-width="1.6"/></svg>Solve problems in an unfamiliar and challenging<br>outdoor environment</li>
    </ul>
    <p>Our tours have many great popular NZ tourist activities but more<br>importantly go where no other similar tours go. We create our<br>own path less travelled!!!</p>
    <p>We also aim to keep driving/travel to a minumum. Through<br>experience we know this means more time having fun ; )</p>
    <div class="card-cta">Sound good?...<br>Check out our new Tours on Offer……..</div>
  </section>

  <h2 class="panel-title"><span>We are the only adventure</span><span>tour organization provid-</span><span>ing exciting experiences on</span><span>and off the beaten track</span></h2>
  <div class="panel-body">
    <p><span>We are all about making your story in NZ one worth telling. Here at ………….</span><span>Tours we pride ourselves in providing the most memorable and exciting</span><span>adventure based tours for students JUST LIKE YOU. We don’t justtake you</span><span>to some of New Zealand’s world-class adventure activities, we also take you</span><span>deeper into the real New Zealand other tours don’t touch.</span></p>
    <p><span>Our guides are addicted to adventure and the outdoors. We are ready to</span><span>have some fun and share with you our knowledge of our beautiful country.</span><strong>Come and get into it!</strong></p>
  </div>

  <div class="photo photo-group"><div class="fill" role="img" aria-label="Photo of a tour group gathered by a lake shore next to kayaks"></div></div>

  <footer class="footer">
    <div class="brand"><span class="brand-dot"></span><span>Trailmark<br>Tours</span></div>
    <div class="divider"></div>
    <div class="contact">CONTACT<strong>ROWAN ASHBY</strong></div>
  </footer>
</main>
</body>
</html>
```